Brightpath Wellness Referral Program

We have recently started a referral program for our clinics and we need a postcard that we can hand our to clients to let them know about the new program.
We are looking for a 4x6" card design that highlights our incentive referral program while visually either showing some of the services we offer, or, conveying a message of health, community, family, etc.
The details of our referral program can be found at:
https://brightpathwellness.ca/about/refer-a-friend.html
We would also like to see somewhere on the card, 2 lines for:
1) Your name: ( new clients name)
2) Referred by: __________
The card can be single or double sided, whatever looks best for design purposes.
Target Market(s)
Ages 20-50, equal men and women
Look and feel
Each slider illustrates characteristics of the customer's brand and the style your logo design should communicate.

```html
<!DOCTYPE html>
<html lang="en">
<head>
<meta charset="utf-8">
<title>Brightpath Wellness Referral Card</title>
<link href="https://fonts.googleapis.com/css2?family=Mulish:wght@400;600;700&family=Roboto+Condensed:wght@300;400&display=swap" rel="stylesheet">
<style>
  :root {
    --brand-blue: #1b5fab;
    --ink: #1f1f1f;
    --muted: #6c6c6c;
    --fine: #7a7a7a;
    --panel: #ececec;
    --field: #eeeeee;
    --card: #ffffff;
    --backdrop-a: #f6f6f6;
    --backdrop-b: #e6e6e6;
    --gold-light: #ecc866;
    --gold-dark: #c08f2c;
    --silver-light: #d6d6d6;
    --silver-dark: #a3a3a3;
  }
  * { box-sizing: border-box; margin: 0; padding: 0; }
  html, body { width: 1200px; height: 805px; overflow: hidden; }
  body {
    position: relative;
    background: linear-gradient(135deg, var(--backdrop-a), var(--backdrop-b));
    font-family: "Mulish", sans-serif;
    color: var(--ink);
  }
  .card {
    position: absolute;
    top: 76px;
    width: 445px;
    height: 667px;
    background: var(--card);
  }
  .card--front { left: 146px; }
  .card--back { left: 609px; }

  .hero-photo {
    position: absolute; left: 0; top: 0; width: 445px; height: 328px;
    background: linear-gradient(160deg, #d9dde0 0%, #c9a68a 45%, #8a5e44 80%, #2e2826 100%);
  }
  .headline {
    position: absolute; left: 54px; top: 360px;
    font-size: 34px; line-height: 42px; font-weight: 400;
    color: var(--brand-blue); letter-spacing: 0.2px;
  }
  .intro {
    position: absolute; left: 54px; top: 462px; width: 320px;
    font-size: 12px; line-height: 15.6px; color: var(--muted); letter-spacing: 0.3px;
    white-space: nowrap;
  }
  .intro p + p { margin-top: 15px; }
  .site-url {
    position: absolute; left: 54px; top: 621px;
    font-size: 9.5px; color: var(--muted); letter-spacing: 0.2px;
  }
  .brand {
    position: absolute; right: 45px; top: 607px;
    display: flex; align-items: center; gap: 6px;
    font-size: 14px; font-weight: 600; color: var(--brand-blue);
  }
  .brand-dot { width: 18px; height: 18px; border-radius: 50%; background: var(--brand-blue); }

  .reward {
    position: absolute; left: 36px; width: 373px; height: 126px;
    background: var(--panel);
  }
  .reward--gold { top: 34px; }
  .reward--silver { top: 169px; }
  .reward-art {
    position: absolute; left: 14px; top: 8px; width: 96px; height: 96px;
  }
  .reward--gold .reward-art { background: linear-gradient(135deg, var(--gold-light), var(--gold-dark)); }
  .reward--silver .reward-art { background: linear-gradient(135deg, var(--silver-light), var(--silver-dark)); }
  .reward-amount {
    position: absolute; left: 143px; top: 20px;
    font-size: 32px; font-weight: 400; color: var(--brand-blue); letter-spacing: 0.3px;
  }
  .reward-amount sup { font-size: 18px; vertical-align: 12px; }
  .reward-note {
    position: absolute; left: 143px; top: 72px; width: 225px;
    font-size: 10.5px; line-height: 15.6px; letter-spacing: 0.2px;
  }
  .credits {
    position: absolute; left: 53px; top: 327px; width: 370px;
    font-size: 11px; line-height: 18.6px; letter-spacing: 0.1px; white-space: nowrap;
  }
  .credits strong { font-weight: 700; }

  .field {
    position: absolute; height: 32px; background: var(--field);
    font-size: 11px; line-height: 32px; padding-left: 14px;
  }
  .field--name { left: 32px; top: 430px; width: 373px; }
  .field--referrer { left: 32px; top: 470px; width: 373px; }
  .field--date { left: 32px; top: 510px; width: 181px; }
  .field--location { left: 224px; top: 510px; width: 181px; }

  .fine-print {
    position: absolute; left: 21px; top: 572px; width: 410px;
    font-family: "Roboto Condensed", sans-serif; font-weight: 300;
    font-size: 7.4px; line-height: 11.1px; color: var(--fine); letter-spacing: -0.1px;
  }
  .fine-print::before { content: ""; float: right; width: 0; height: 34px; }
  .fine-print-gap { float: right; clear: right; width: 52px; height: 44px; }
  .corner-dot {
    position: absolute; right: 22px; top: 620px;
    width: 26px; height: 26px; border-radius: 50%; background: var(--brand-blue);
  }
</style>
</head>
<body>
  <section class="card card--front">
    <div class="hero-photo" role="img" aria-label="Massage therapist's hands working on a client's back"></div>
    <h1 class="headline">Good people,<br>know good people</h1>
    <div class="intro">
      <p>Referrals are the lifeblood of our small business.</p>
      <p>We are incredibly grateful for your trust and<br>recommendations over the years,and we want to<br>show our gratitude. That's why we are introducing<br>an excitingnew way to earn more free treatment.</p>
    </div>
    <div class="site-url">www.brightpathwellness.ca</div>
    <div class="brand"><span class="brand-dot"></span>Brightpath Wellness</div>
  </section>

  <section class="card card--back">
    <div class="reward reward--gold">
      <div class="reward-art" role="img" aria-label="Gold star illustration"></div>
      <div class="reward-amount">Earn $25<sup>*</sup></div>
      <p class="reward-note">for every referral you make to our south Calgary location (Southland Drive), and;</p>
    </div>
    <div class="reward reward--silver">
      <div class="reward-art" role="img" aria-label="Silver star illustration"></div>
      <div class="reward-amount">Earn $10<sup>*</sup></div>
      <p class="reward-note">for every referral you make to our north Calgary location (Evanston).</p>
    </div>

    <p class="credits">Credits can be <strong>used for any service at either our north or south</strong><br><strong>location</strong> and, in the spirit of community, <strong>credits are transferable.</strong><br>Refer 4 people to thesouth and you could gift someone a $100 gift<br>card! Or, enjoy a well deserved,free treatment yourself.</p>

    <div class="field field--name">Your name</div>
    <div class="field field--referrer">Referred by</div>
    <div class="field field--date">Date</div>
    <div class="field field--location">Location</div>

    <p class="fine-print"><span class="fine-print-gap"></span>*Referral(s) must be brand new client(s) to the Brightpath Wellness Inc. practice, having never booked or attended an appointment at any Brightpath Wellness location. Referral must attend their appointment for you to be eligible for a referral credit. Referral credit value is dependent upon which Brightpath Wellness location your referral attends: you are eligible for a $10 credit for a referral to our north location (#410 - 1550 Ridgeview Parkway NW); you are eligible for a $25 credit for a referral to our south location (#120 - 7740 Lakeshore Drive SE). We are really good at asking but please remind your referral to tell us it is YOU who we have to thank! Credit(s) may be redeemed as payment or partial payment for any service at any Brightpath Wellness location. Credits have no cash value and no expiry.</p>
    <div class="corner-dot"></div>
  </section>
</body>
</html>
```